Stationary/business card for Custom Home builder
Pemberton Dwellings General Contractor
Simple
Travis Lindqvist
president
817 Calder Meadow Road
Dorrance Crossing, SC 29871
kbarlowbuilds@mailvero.net
Please use my logo

```html
<!DOCTYPE html>
<html lang="en">
<head>
<meta charset="utf-8">
<title>Pemberton Dwellings – Business Card</title>
<link rel="stylesheet" href="https://fonts.googleapis.com/css2?family=Cinzel:wght@400;600&display=swap">
<style>
  :root {
    --page: #eef0f2;
    --card-white: #ffffff;
    --brand-blue: #1f8fd6;
    --brand-blue-light: #3fb0ee;
    --brand-blue-deep: #136fb0;
    --ink-navy: #1b3f66;
    --ink-grey: #4a5562;
    --swoosh-black: #111418;
  }
  html, body {
    margin: 0;
    padding: 0;
    width: 1200px;
    height: 980px;
    overflow: hidden;
    background: var(--page);
    font-family: "Cinzel", "Times New Roman", serif;
  }
  .sheet {
    width: 1200px;
    height: 980px;
    display: flex;
    flex-direction: column;
    align-items: center;
    justify-content: space-evenly;
  }
  .card {
    position: relative;
    width: 760px;
    height: 434px;
    border-radius: 22px;
    overflow: hidden;
    box-shadow: 0 6px 18px rgba(0,0,0,0.12);
  }
  .card svg.card-art { position: absolute; inset: 0; }

  /* Front */
  .card-front { background: var(--card-white); }
  .contact-list {
    position: absolute;
    left: 46px;
    top: 34px;
    margin: 0;
    padding: 0;
    list-style: none;
    font-size: 12px;
    letter-spacing: 0.06em;
    color: var(--ink-grey);
    line-height: 20px;
  }
  .contact-list li { display: flex; align-items: center; gap: 10px; }
  .contact-dot {
    width: 11px; height: 11px; border-radius: 50%;
    background: var(--brand-blue-deep);
    flex: none;
  }
  .brand-lockup {
    position: absolute;
    right: 48px;
    top: 200px;
    text-align: center;
    color: var(--ink-navy);
  }
  .brand-name {
    font-size: 34px;
    font-weight: 600;
    letter-spacing: 0.02em;
    margin: 0;
    line-height: 1;
    display: flex;
    align-items: center;
    gap: 12px;
  }
  .brand-mark {
    width: 16px; height: 16px; border-radius: 50%;
    background: var(--brand-blue);
    flex: none;
  }
  .brand-tagline {
    margin: 8px 0 0;
    font-size: 15px;
    font-weight: 600;
    letter-spacing: 0.22em;
  }
  .holder {
    position: absolute;
    right: 44px;
    bottom: 26px;
    text-align: right;
    color: var(--card-white);
  }
  .holder-name { font-size: 17px; letter-spacing: 0.08em; margin: 0; }
  .holder-title { font-size: 11px; letter-spacing: 0.16em; margin: 3px 0 0; opacity: 0.9; }

  /* Back */
  .card-back {
    background: radial-gradient(ellipse at 50% 40%, var(--brand-blue-light) 0%, var(--brand-blue) 55%, var(--brand-blue-deep) 100%);
  }
  .back-brand {
    position: absolute;
    left: 0; right: 0;
    top: 180px;
    display: flex;
    justify-content: center;
    align-items: center;
    gap: 14px;
    color: var(--card-white);
    font-size: 40px;
    font-weight: 600;
    letter-spacing: 0.02em;
  }
  .back-brand .brand-mark { background: var(--card-white); width: 20px; height: 20px; }
  .back-web {
    position: absolute;
    left: 46px;
    bottom: 30px;
    color: var(--card-white);
    font-size: 13px;
    letter-spacing: 0.14em;
  }
</style>
</head>
<body>
<main class="sheet">

  <section class="card card-back" aria-label="Business card back">
    <div class="back-brand"><span class="brand-mark"></span>Pemberton Dwellings</div>
    <div class="back-web">www.calderbuildsample.com</div>
  </section>

  <section class="card card-front" aria-label="Business card front">
    <svg class="card-art" viewBox="0 0 760 434" preserveAspectRatio="none" aria-hidden="true">
      <path d="M0,318 C210,262 470,420 760,332 L760,434 L0,434 Z" fill="var(--brand-blue)"/>
      <path d="M0,300 C210,246 470,404 760,316 L760,328 C470,414 210,258 0,314 Z" fill="var(--swoosh-black)"/>
      <path d="M0,286 C210,234 470,392 760,304 L760,308 C470,396 210,238 0,290 Z" fill="var(--brand-blue-light)"/>
    </svg>

    <ul class="contact-list">
      <li><span class="contact-dot"></span>817 Calder Meadow Road</li>
      <li><span class="contact-dot"></span>Dorrance Crossing, SC 29871</li>
      <li><span class="contact-dot"></span>843-555-0142</li>
      <li><span class="contact-dot"></span>843-555-0187</li>
      <li><span class="contact-dot"></span>843-555-0163</li>
      <li><span class="contact-dot"></span>kbarlowbuilds@mailvero.net</li>
      <li><span class="contact-dot"></span>www.calderbuildsample.com</li>
    </ul>

    <div class="brand-lockup">
      <p class="brand-name"><span class="brand-mark"></span>Pemberton Dwellings</p>
      <p class="brand-tagline">General Contractor</p>
    </div>

    <div class="holder">
      <p class="holder-name">Travis Lindqvist</p>
      <p class="holder-title">President</p>
    </div>
  </section>

</main>
</body>
</html>
```